Wakeboarding and Aqua Park front cover for flyer

I would like a front cover that I can use on a DL flyer to advertise both our Aqua Park and Cable Ski. The design should reflect the fun nature of our activity and appeal to both families and young people (18-30) but with may be a touch of an extreme sports feel.

I would like two pictures to be visible, one of the Aqua Park and the other the cable ski plus our logo. Both should have prominence but if the design has one at the top and the other at the bottom please put the Aqua Park at the top as this is currently our most popular activity.

There should be some text visible near the Aqua Park picture saying:

AQUA PARK
"Bigger and Better for 2017!"

There should be some text visible near/over the Cable Ski picture saying:

CABLE SKI
"Try kneeboarding, water skiing or wakeboarding this summer!"

Target Market(s)

Young people, families

Industry/Entity Type

Entertainment

Colors
0255a3
fbed22
fbee3e
0692cd

Requirements
Must have
• Picture of wakeboarding, picture of Aqua Park
Nice to have
• nice vibrant blues and yellows. illustration.
Should not have
• Have included a few extra aqua park images now in case they look better than the first one uploaded. Don't need to include them all though.

```html
<!DOCTYPE html>
<html lang="en">
<head>
<meta charset="utf-8">
<title>Northvale Cablewake – DL Flyer Cover</title>
<link rel="stylesheet" href="https://fonts.googleapis.com/css2?family=Audiowide&family=Exo+2:wght@600;700;800&display=swap">
<style>
  :root {
    --brand-blue: #0255a3;
    --deep-blue: #013f7c;
    --sky-blue: #0692cd;
    --brand-yellow: #fbed22;
    --soft-yellow: #fbee3e;
    --warm-yellow: #f5c400;
    --ink: #111111;
    --white: #ffffff;
    --stage: #3a3a3a;
  }
  * { margin: 0; padding: 0; box-sizing: border-box; }
  html, body {
    width: 902px; height: 1200px; overflow: hidden;
    background: var(--stage);
  }
  .flyer {
    position: absolute; left: 171px; top: 27px;
    width: 560px; height: 1145px; overflow: hidden;
    background: radial-gradient(ellipse at 50% 0%, var(--soft-yellow) 0%, var(--brand-yellow) 45%, var(--warm-yellow) 100%);
    font-family: "Exo 2", sans-serif;
  }
  .flyer-shapes, .aqua-photo { position: absolute; left: 0; top: 0; }
  .brand-name {
    position: absolute; top: 38px; left: 0; width: 100%;
    display: flex; justify-content: center; align-items: center; gap: 12px;
  }
  .brand-name__mark { width: 26px; height: 26px; background: var(--ink); }
  .brand-name__text {
    font-weight: 800; font-size: 34px; line-height: 0.92; color: var(--ink);
    text-transform: lowercase; letter-spacing: 0.5px;
  }
  .aqua-headline {
    position: absolute; top: 432px; left: 0; width: 490px; text-align: center;
    font-family: "Audiowide", sans-serif;
  }
  .aqua-headline__lead {
    font-size: 33px; color: #1a1a1a; -webkit-text-stroke: 1.6px var(--white);
    letter-spacing: 0.5px; line-height: 1.1;
  }
  .aqua-headline__year { font-size: 46px; color: var(--brand-yellow); line-height: 1.15; }
  .cable-photo {
    position: absolute; left: 43px; top: 588px; width: 464px; height: 243px;
    border: 4px solid var(--white); border-radius: 16px;
    background: linear-gradient(180deg, #c9dbe8 0%, #5f8a4e 30%, #7c9aa8 48%, #a8c1cf 70%, #6e8fa3 100%);
    box-shadow: 0 3px 8px rgba(0,0,0,0.35);
  }
  .cable-tagline {
    position: absolute; top: 852px; left: 0; width: 560px; text-align: center;
    font-weight: 700; font-size: 25px; line-height: 32px; letter-spacing: 0.5px;
    text-transform: uppercase; color: var(--brand-yellow);
  }
  .cable-tagline__end { color: var(--white); }
  .contact {
    position: absolute; top: 978px; left: 0; width: 560px; text-align: center;
  }
  .contact__title { font-weight: 700; font-size: 29px; color: var(--brand-blue); line-height: 1.1; }
  .contact__phone {
    display: flex; justify-content: center; align-items: center; gap: 10px;
    font-weight: 700; font-size: 48px; color: var(--ink); line-height: 1.05;
  }
  .contact__rule { width: 368px; height: 2px; background: var(--brand-blue); margin: 6px auto 0; }
  .contact__web {
    display: flex; justify-content: center; align-items: center; gap: 8px;
    font-weight: 700; font-size: 19px; color: var(--ink); margin-top: 6px;
  }
</style>
</head>
<body>
<div class="flyer">
  <svg class="flyer-shapes" width="560" height="1145" viewBox="0 0 560 1145">
    <path d="M0,540 L330,575 C450,575 520,470 535,370 C545,330 560,300 560,300 V1000 C420,960 150,960 0,1010 Z" fill="var(--brand-blue)"/>
    <path d="M330,575 C450,575 525,470 540,360 L560,330 V420 C540,500 470,590 330,590 Z" fill="var(--brand-yellow)"/>
    <path d="M0,1010 C150,960 420,960 560,1000" fill="none" stroke="var(--deep-blue)" stroke-width="6"/>
  </svg>

  <svg class="aqua-photo" width="560" height="600" viewBox="0 0 560 600" role="img" aria-label="Photo of the inflatable aqua park on the lake, a visitor leaping from the tall climbing tower under a blue summer sky">
    <defs>
      <linearGradient id="aquaTones" x1="0" y1="0" x2="0" y2="1">
        <stop offset="0" stop-color="#3f86c9"/>
        <stop offset="0.35" stop-color="#9ec4e3"/>
        <stop offset="0.6" stop-color="#2c4d7a"/>
        <stop offset="0.75" stop-color="#141c26"/>
        <stop offset="1" stop-color="#050608"/>
      </linearGradient>
    </defs>
    <path d="M0,127 H380 C470,127 517,230 517,340 C517,460 450,565 330,565 H0 Z" fill="url(#aquaTones)" stroke="var(--white)" stroke-width="6"/>
  </svg>

  <div class="brand-name">
    <span class="brand-name__mark"></span>
    <span class="brand-name__text">northvale<br>cablewake</span>
  </div>

  <div class="aqua-headline">
    <div class="aqua-headline__lead">BIGGER AND BETTER</div>
    <div class="aqua-headline__year">FOR 2017!</div>
  </div>

  <div class="cable-photo" role="img" aria-label="Photo of a cable skier in a helmet carving across the lake with spray, trees and clubhouse behind"></div>

  <p class="cable-tagline">Try kneeboarding, water<br>skiing or wakeboarding<br><span class="cable-tagline__end">this summer!</span></p>

  <div class="contact">
    <div class="contact__title">Contact Us</div>
    <div class="contact__phone">
      <svg width="28" height="28" viewBox="0 0 28 28" aria-hidden="true">
        <circle cx="14" cy="14" r="12.5" fill="none" stroke="var(--white)" stroke-width="2"/>
        <path d="M9.5,7.5 l3,3 -1.6,1.8 c0.9,1.9 2.2,3.2 4,4.1 l1.8,-1.6 3,3 -1.6,2 c-4.8,-0.6 -9.6,-5.4 -10.2,-10.2 z" fill="var(--white)"/>
      </svg>
      <span>1234567890</span>
    </div>
    <div class="contact__rule"></div>
    <div class="contact__web">
      <svg width="14" height="14" viewBox="0 0 14 14" aria-hidden="true">
        <g fill="none" stroke="var(--white)" stroke-width="1.2">
          <circle cx="7" cy="7" r="6"/><ellipse cx="7" cy="7" rx="2.6" ry="6"/><path d="M1,7 H13"/>
        </g>
      </svg>
      <span>www.websiteaddress.com</span>
    </div>
    <div class="contact__rule"></div>
  </div>
</div>
</body>
</html>
```